Business Card Design

Contact Information for Business Card

A vertical business card request- a medium & light gray with silverpine tree logo (logo is attached)

Please use Trebuchet font -- if possible- can we use two different color gray? (See pictures attached below)
Info on the front should be the Silverpine tree logo - on the top of the card, followed by the info ...
Card to read: " " indicated what should be on the card --
Name: " Carla Merrow "
Title : "Partner "
" Office: 202.555.0147 "
" Mobile: 202.555.0183 "

Backside of the card - solid medium color gray color w/ address and small message centered in the card - Trebuchet font
to read:

" 718 B North Larkmoor Avenue, NE "
" Washington, DC 20019 "

Then below address to read:
" Fundraising | Event Planning | Political Consulting "

```html
<!DOCTYPE html>
<html lang="en">
<head>
<meta charset="utf-8">
<title>Silverpine Strategies – Business Card</title>
<link rel="stylesheet" href="https://fonts.googleapis.com/css2?family=PT+Sans+Narrow:wght@400;700&display=swap">
<style>
  :root {
    --gray-dark: #545454;
    --gray-medium: #77787b;
    --gray-light: #e6e7e8;
    --emblem-area: #5e5e5e;
    --ink: #333333;
    --brand-tone: #c8c8c8;
    --white: #ffffff;
    --frame: #3a3a3a;
  }
  * { box-sizing: border-box; margin: 0; padding: 0; }
  html, body {
    width: 1200px; height: 1000px; overflow: hidden;
    background: var(--white);
  }
  .canvas {
    position: relative; width: 1200px; height: 1000px;
    border: 1px solid var(--frame);
    font-family: "PT Sans Narrow", "Trebuchet MS", sans-serif;
    overflow: hidden;
  }

  /* Front of card */
  .card-front {
    position: absolute; left: 0; top: 0; width: 568px; height: 995px;
    background: var(--gray-light);
    border-right: 1px solid #cfcfcf;
  }
  .card-front__wave { position: absolute; left: 0; top: 0; width: 568px; height: 600px; }
  .emblem-area {
    position: absolute; left: 195px; top: 85px; width: 330px; height: 300px;
    background: var(--emblem-area);
  }
  .brand {
    position: absolute; left: 28px; top: 388px; width: 528px;
    color: var(--brand-tone); font-weight: 400;
  }
  .brand__name {
    display: block; font-size: 82px; line-height: 72px;
    letter-spacing: 9px; text-align: center;
  }
  .brand__sub {
    display: block; font-size: 36px; line-height: 40px;
    letter-spacing: 3px; text-align: right;
  }
  .identity {
    position: absolute; left: 0; top: 668px; width: 568px;
    text-align: center; color: var(--ink);
  }
  .identity__name, .identity__title { font-size: 44px; line-height: 54px; font-weight: 400; }
  .contact {
    position: absolute; left: 0; top: 814px; width: 568px;
    text-align: center; color: var(--ink);
    font-size: 41px; line-height: 45px; font-weight: 700; letter-spacing: 1.5px;
  }

  /* Back of card */
  .card-back {
    position: absolute; left: 612px; top: 0; width: 566px; height: 993px;
    background: var(--gray-medium);
  }
  .address {
    position: absolute; left: 0; top: 408px; width: 566px;
    text-align: center; color: var(--white); font-style: normal;
    font-size: 37px; line-height: 40px; letter-spacing: 0.8px;
  }
  .services {
    position: absolute; left: 0; top: 877px; width: 566px; height: 78px;
    background: var(--white);
    display: flex; align-items: center; justify-content: center;
    color: var(--ink); font-weight: 700; font-size: 22px; letter-spacing: 0.6px;
  }
  .services__divider {
    display: inline-block; width: 3px; height: 28px; background: var(--ink);
    margin: 0 3px;
  }
</style>
</head>
<body>
  <div class="canvas">
    <section class="card-front">
      <svg class="card-front__wave" viewBox="0 0 568 600" aria-hidden="true">
        <path d="M0 0 H568 V552 C440 505 300 490 0 552 Z" fill="var(--gray-dark)"/>
        <path d="M0 560 C300 498 440 513 568 560" fill="none" stroke="var(--white)" stroke-width="14"/>
      </svg>
      <div class="emblem-area" role="img" aria-label="Company emblem area"></div>
      <div class="brand">
        <span class="brand__name">SILVERPINE</span>
        <span class="brand__sub">STRATEGIES</span>
      </div>
      <div class="identity">
        <p class="identity__name">CARLA MERROW</p>
        <p class="identity__title">PARTNER</p>
      </div>
      <div class="contact">
        <p>OFFICE: 202.555.0147</p>
        <p>MOBILE: 202.555.0183</p>
      </div>
    </section>

    <section class="card-back">
      <address class="address">
        718 B North Larkmoor Avenue, NE<br>
        Washington DC 20019
      </address>
      <div class="services">
        FUNDRAISING<span class="services__divider"></span>EVENT PLANNING<span class="services__divider"></span>POLITICAL CONSULTING
      </div>
    </section>
  </div>
</body>
</html>
```